WEB PAGES DESIGN

We need a web design for a new company called "NEXO47". Our major business is that provide Internet Data Center solution, such as: rack/colocation, bandwidth, dedicated server, cloud server, CDN, and so on.
Requirements of Design:
1. Home page layout can refer to index-content.jpg in the attachments, but not limited.
2. According to match logo colors to design colors of web pages, Logo in the attachments.
3. The web contents of home page in image of the index-content.jpg.
4. The successful bidder will need to design three banner.

```html
<!DOCTYPE html>
<html lang="en">
<head>
<meta charset="utf-8">
<title>NEXO47 – IDC Solutions</title>
<link rel="stylesheet" href="https://fonts.googleapis.com/css2?family=Open+Sans:wght@400;600;700&family=Roboto:wght@400;500;700&display=swap">
<style>
:root{
  --green:#8dc63f;
  --green-dark:#79b12c;
  --orange:#f7941d;
  --orange-light:#fdb44b;
  --ink:#333333;
  --muted:#666666;
  --topbar:#efefef;
  --line:#dddddd;
  --footer:#333333;
  --footer-text:#c9c9c9;
  --white:#ffffff;
}
*{box-sizing:border-box;margin:0;padding:0}
html,body{width:895px;height:1200px;overflow:hidden}
body{position:relative;background:var(--white);font-family:"Open Sans",Arial,sans-serif;color:var(--ink)}
.abs{position:absolute}
a{color:inherit;text-decoration:none}

/* top bar */
.topbar{left:0;top:0;width:895px;height:24px;background:var(--topbar);font-size:10px;color:var(--ink)}
.topbar .phone{left:41px;top:4px;display:flex;align-items:center;gap:6px}
.topbar .phone small{color:var(--muted);font-size:10px;margin-left:4px}
.topbar .account{left:682px;top:4px;display:flex;align-items:center;gap:14px}
.topbar .account span{display:flex;align-items:center;gap:4px}
.topbar .socials{left:783px;top:5px;display:flex;gap:9px}
.topbar .socials i{display:block;width:11px;height:11px;background:var(--ink);border-radius:2px}
.topbar .sep{width:1px;height:14px;background:#ccc}

/* header */
.header{left:0;top:24px;width:895px;height:70px;background:var(--white)}
.brand{left:42px;top:20px;display:flex;align-items:center;gap:8px}
.brand-mark{width:32px;height:32px;background:var(--green)}
.brand-name{font-family:"Roboto",Arial,sans-serif;font-weight:700;font-size:17px;color:#3c3c3c;letter-spacing:.5px}
.nav{left:263px;top:19px;height:32px;font-family:"Roboto",Arial,sans-serif;font-size:12.5px;font-weight:500;color:var(--ink)}
.nav a{position:absolute;top:0;height:32px;line-height:32px;white-space:nowrap}
.nav .active{background:var(--green);color:var(--white);width:70px;text-align:center}

/* hero */
.hero{left:0;top:94px;width:895px;height:344px;background:var(--green)}
.hero h1{left:41px;top:52px;font-size:36px;font-weight:700;color:var(--white);letter-spacing:.5px}
.hero .lead{left:41px;top:104px;width:560px;font-size:16.5px;font-weight:600;line-height:21px;color:var(--white)}
.hero ul{left:41px;top:162px;list-style:none;font-size:11.5px;font-weight:600;color:var(--white)}
.hero li{display:flex;align-items:center;gap:8px;height:26.5px}
.btn-orange{display:block;background:linear-gradient(var(--orange-light),var(--orange));border:1px solid #e0821a;color:#222;font-weight:700;text-align:center}
.hero .learn{left:41px;top:252px;width:107px;height:32px;line-height:30px;font-size:12.5px}
.hero-photo{left:558px;top:8px;width:289px;height:336px;background:linear-gradient(180deg,#6fa42c 0%,#2c2c2c 55%,#222 100%);border-radius:120px 120px 0 0}
.slider-arrow{top:158px;width:26px;height:26px;border-radius:50%;background:rgba(60,60,60,.55)}

/* section titles */
.section-title{left:0;width:895px;text-align:center;font-family:"Roboto",Arial,sans-serif;font-size:28px;color:var(--ink)}
.section-title b{font-weight:700}
.title-rule{left:305px;width:250px;height:2px;background:var(--green)}

/* offer cards */
.card{top:536px;width:193px;height:192px;border:2px solid #e3e3e3;text-align:center;background:var(--white)}
.card h3{margin-top:17px;font-family:"Roboto",Arial,sans-serif;font-weight:500;font-size:16.5px;color:var(--ink)}
.card .price{margin-top:8px;font-size:11px}
.card .price strong{color:var(--green);font-size:17px;font-weight:700}
.card p{margin:10px auto 0;width:170px;font-size:10.5px;line-height:15px}
.card .plans{position:absolute;left:40px;top:145px;width:110px;height:26px;line-height:26px;background:var(--green);color:var(--white);font-size:11.5px;font-weight:600}
.card.featured{background:var(--green);border-color:var(--green);color:var(--white)}
.card.featured h3,.card.featured .price strong{color:var(--white)}
.card.featured .plans{background:var(--white);color:var(--ink)}

/* partners */
.partner{top:826px;width:124px;height:55px;border:2px solid #e6e6e6;display:flex;align-items:center;justify-content:center}
.partner i{display:block;width:80px;height:18px;background:#9a9a9a;border-radius:3px}

/* cta band */
.cta{left:0;top:908px;width:895px;height:86px;background:var(--green)}
.cta h2{left:41px;top:29px;font-size:21px;font-weight:700;color:var(--white)}
.cta .phone{left:508px;top:29px;display:flex;align-items:center;gap:6px;font-size:19px;color:#1e1e1e}
.cta .contact-btn{left:701px;top:28px;width:145px;height:30px;line-height:28px;font-size:12.5px}

/* footer */
.footer{left:0;top:994px;width:895px;height:206px;background:var(--footer);color:var(--footer-text)}
.fcol{top:19px;font-size:9.5px}
.fcol h4{font-family:"Roboto",Arial,sans-serif;font-size:12.5px;font-weight:500;color:var(--white);margin-bottom:8px}
.fcol li{list-style:none;height:16.5px}
.fcol.low{top:24px}
.fcol .row{display:flex;gap:8px;margin-bottom:10px;line-height:13px}
.footer .rule{left:41px;top:154px;width:813px;height:1px;background:#4a4a4a}
.footer .copy{left:41px;top:175px;font-size:9.5px;color:var(--white)}
.footer .pay{left:358px;top:168px;display:flex;gap:9px}
.footer .pay i{display:block;width:38px;height:24px;background:#e8e8e8;border-radius:3px}
.footer .pay i.wide{width:60px;background:none;border:1px solid #777}
.footer .social{left:742px;top:169px;display:flex;gap:10px}
.footer .social i{display:block;width:21px;height:21px;border-radius:50%;background:#4d7fb5}
</style>
</head>
<body>

<div class="abs topbar">
  <div class="abs phone">
    <svg width="14" height="12" viewBox="0 0 14 12"><path d="M1 4c0-3 12-3 12 0v1h-3V3.5H4V5H1z" fill="#5a9e2a"/><rect x="3" y="6" width="8" height="5" rx="1" fill="#5a9e2a"/></svg>
    <span>555-201-4470</span><small>24/7 Support</small>
  </div>
  <div class="abs account">
    <span><svg width="11" height="11" viewBox="0 0 11 11"><circle cx="5.5" cy="3.2" r="2.7" fill="#8dc63f"/><path d="M0 11c0-4 11-4 11 0z" fill="#8dc63f"/></svg>Login</span>
    <span>Register</span>
  </div>
  <div class="abs socials"><i></i><i></i><i></i><i></i></div>
</div>

<header class="abs header">
  <div class="abs brand"><div class="brand-mark"></div><span class="brand-name">NEXO47</span></div>
  <nav class="abs nav">
    <a class="active" style="left:0">HOME</a>
    <a style="left:89px">DEDICATED SERVER</a>
    <a style="left:228px">HOSTING</a>
    <a style="left:314px">DATA CENTERS</a>
    <a style="left:431px">ABOUT US</a>
    <a style="left:523px">CONTACT US</a>
  </nav>
</header>

<section class="abs hero">
  <h1 class="abs">IDC SOLUTIONS</h1>
  <p class="abs lead">NEXO47 provides a wide range of highly specialized solutions that utilizes technology to transform your organization.</p>
  <ul class="abs">
    <li><svg width="13" height="13" viewBox="0 0 13 13"><circle cx="6.5" cy="6.5" r="6.5" fill="#fff"/><path d="M3.5 6.7l2 2 4-4.2" stroke="#8dc63f" stroke-width="1.8" fill="none"/></svg>Unlimited Bandwidth with Massive Storage</li>
    <li><svg width="13" height="13" viewBox="0 0 13 13"><circle cx="6.5" cy="6.5" r="6.5" fill="#fff"/><path d="M3.5 6.7l2 2 4-4.2" stroke="#8dc63f" stroke-width="1.8" fill="none"/></svg>Unlimited Databases and Email Addresses</li>
    <li><svg width="13" height="13" viewBox="0 0 13 13"><circle cx="6.5" cy="6.5" r="6.5" fill="#fff"/><path d="M3.5 6.7l2 2 4-4.2" stroke="#8dc63f" stroke-width="1.8" fill="none"/></svg>99.99% Uptime Guarantee &amp; 24/7 Support</li>
  </ul>
  <a class="abs btn-orange learn">LEARN MORE</a>
  <div class="abs hero-photo" role="img" aria-label="Photo of a smiling businessman in a dark suit with arms crossed"></div>
  <svg class="abs slider-arrow" style="left:6px" viewBox="0 0 26 26"><path d="M15 8l-5 5 5 5" stroke="#fff" stroke-width="2.2" fill="none"/></svg>
  <svg class="abs slider-arrow" style="left:862px" viewBox="0 0 26 26"><path d="M11 8l5 5-5 5" stroke="#fff" stroke-width="2.2" fill="none"/></svg>
</section>

<h2 class="abs section-title" style="top:466px;font-weight:400">WHAT WE <b>OFFER</b></h2>
<div class="abs title-rule" style="top:506px"></div>

<div class="abs card" style="left:41px">
  <h3>DEDICATED SERVERS</h3>
  <div class="price">Start at <strong>$18.99</strong> / month</div>
  <p>Lorem ipsum dolor sit amet sit et justo con sectetuer adipiscing elit. Suspendisse et justo Praesent mattis.</p>
  <a class="plans">View all Plans</a>
</div>
<div class="abs card featured" style="left:247px">
  <h3>SERVERS HOSTING</h3>
  <div class="price">Start at <strong>$18.99</strong> / month</div>
  <p>Lorem ipsum dolor sit amet sit et justo con sectetuer adipiscing elit. Suspendisse et justo Praesent mattis.</p>
  <a class="plans">View all Plans</a>
</div>
<div class="abs card" style="left:454px">
  <h3>RACK &amp; BANDWIDTH</h3>
  <div class="price">Start at <strong>$18.99</strong> / month</div>
  <p>Lorem ipsum dolor sit amet sit et justo con sectetuer adipiscing elit. Suspendisse et justo Praesent mattis.</p>
  <a class="plans">View all Plans</a>
</div>
<div class="abs card" style="left:660px">
  <h3>RESELLER &amp; REFERRAL</h3>
  <div class="price">Start at <strong>$18.99</strong> / month</div>
  <p>Lorem ipsum dolor sit amet sit et justo con sectetuer adipiscing elit. Suspendisse et justo Praesent mattis.</p>
  <a class="plans">View all Plans</a>
</div>

<h2 class="abs section-title" style="top:756px;font-weight:400">OUR <b>PARTNERS</b></h2>
<div class="abs title-rule" style="top:796px"></div>

<div class="abs partner" style="left:41px"><i></i></div>
<div class="abs partner" style="left:179px"><i></i></div>
<div class="abs partner" style="left:317px"><i></i></div>
<div class="abs partner" style="left:455px"><i></i></div>
<div class="abs partner" style="left:593px"><i></i></div>
<div class="abs partner" style="left:730px"><i></i></div>

<section class="abs cta">
  <h2 class="abs">Have Questions About Our Services?</h2>
  <div class="abs phone">
    <svg width="20" height="17" viewBox="0 0 14 12"><path d="M1 4c0-3 12-3 12 0v1h-3V3.5H4V5H1z" fill="#1e1e1e"/><rect x="3" y="6" width="8" height="5" rx="1" fill="#1e1e1e"/></svg>
    <span>+1 (555) 201 4471</span>
  </div>
  <a class="abs btn-orange contact-btn">CONTACT US NOW</a>
</section>

<footer class="abs footer">
  <div class="abs fcol" style="left:41px"><h4>OUR SERVICES</h4><ul><li>Web Hosting</li><li>Dedicated Servers</li><li>Servers Hosting</li><li>Rack &amp; Bandwidth</li><li>Reseller &amp; Referral</li></ul></div>
  <div class="abs fcol" style="left:199px"><h4>COMPANY</h4><ul><li>About Us</li><li>Contact Us</li><li>Terms of Service</li><li>Privacy Policy</li><li>Site Map</li></ul></div>
  <div class="abs fcol" style="left:341px"><h4>SUPPORT</h4><ul><li>Live Support</li><li>Forum</li><li>Help / FAQ's</li></ul></div>
  <div class="abs fcol low" style="left:481px"><h4>MY ACCOUNT</h4><ul><li>Member Login</li><li>Register</li><li>My Account</li><li>Order History</li></ul></div>
  <div class="abs fcol low" style="left:710px"><h4>CONTACT US</h4>
    <div class="row"><svg width="9" height="12" viewBox="0 0 9 12"><path d="M4.5 0A4.5 4.5 0 0 0 0 4.5C0 8 4.5 12 4.5 12S9 8 9 4.5A4.5 4.5 0 0 0 4.5 0z" fill="#8dc63f"/><circle cx="4.5" cy="4.5" r="1.7" fill="#333"/></svg><span>88 Harbor Row 9th Floor<br>Portland, OR 97205</span></div>
    <div class="row"><svg width="10" height="10" viewBox="0 0 10 10"><path d="M2 0l2 2.5-1.2 1.3a6 6 0 0 0 3.4 3.4L7.5 6 10 8l-1.5 2C4 10 0 6 0 1.5z" fill="#8dc63f"/></svg><span>+1 (555) 201 4471</span></div>
    <div class="row"><svg width="12" height="9" viewBox="0 0 12 9"><rect width="12" height="9" rx="1" fill="#8dc63f"/><path d="M0.5 1l5.5 4 5.5-4" stroke="#333" fill="none"/></svg><span>info@nexo47.com</span></div>
  </div>
  <div class="abs rule"></div>
  <div class="abs copy">Copyright © 2015 NEXO47. All rights reserved.</div>
  <div class="abs pay"><i></i><i></i><i></i><i></i><i class="wide"></i></div>
  <div class="abs social"><i></i><i style="background:#3aa2d8"></i><i style="background:#2f74a8"></i><i style="background:#c9332c"></i></div>
</footer>

</body>
</html>
```